Creative - Appealing - Business Card Design Project

Looking for a Business card design (vector artwork) for an existing company called 'Copperfield Sound'. We operate in the entertainment industry specializing in audio system design and rental, however; we also deal with other sectors of the entertainment industry including lighting, video, staging and power system design and rental. We would like to see designs that don't focus too much on audio but include elements encompassing everything else.

Double sided business card, following our new colour scheme and logo, which is attached. The card would ideally be creative and eye catching to draw in new customers in the elegant event production market, such as weddings & corporate affairs.

Target Market(s)

High end corporate clients, wedding clients

Industry/Entity Type

Entertainment

Requirements
Must have
• Our contact details, these can be worded & listed however you think appropriate as part as the design

Business Name - Copperfield Sound
My Name - Benedict Thornbury
Web Address - www.copperfieldsound-example.com
Mobile Number - 07914 362 517
Office Number - 0330 411 7785
Email - ben@copperfieldsound-example.com

The name, email and mobile number would need to be able to be changed to my business partners also.

The font used on our logo is Sansation
Nice to have
• On one side maybe a word cloud involving the services in which we can provide; Lighting, Sound, Event Production, Staging, LED Uplighting, Projection Mapping, Wedding Hire

On the other side, all the important credentials of contact.
Should not have
• The design should not use any old style fonts (i.e Times New Roman, Gothic etc) or on the other side of the scale, any 'jokey' fonts (i.e. Comic Sans).

The font to be used is Sansation

```html
<!DOCTYPE html>
<html lang="en">
<head>
<meta charset="utf-8">
<title>Copperfield Sound — Business Card</title>
<link href="https://fonts.googleapis.com/css2?family=Exo+2:wght@400;500;600&display=swap" rel="stylesheet">
<style>
  :root {
    --backdrop: #ecebe8;
    --card-white: #ffffff;
    --card-grey: #8c8c8c;
    --band-grey: #8e8e8e;
    --text-grey: #6f6f71;
    --text-dark: #2a2a2a;
    --brand-purple: #553184;
    --white: #ffffff;
  }
  * { box-sizing: border-box; margin: 0; padding: 0; }
  html, body { width: 1200px; height: 696px; overflow: hidden; }
  body {
    background: var(--backdrop);
    font-family: "Exo 2", "Helvetica Neue", Arial, sans-serif;
    position: relative;
  }
  .card {
    position: absolute;
    top: 180px;
    width: 520px;
    height: 336px;
    border-radius: 22px;
    overflow: hidden;
    box-shadow: 0 6px 18px rgba(0,0,0,0.18);
  }
  /* Front */
  .card--front { left: 50px; background: var(--card-white); }
  .brand {
    position: absolute;
    left: 0; right: 0; top: 62px;
    display: flex; align-items: center; justify-content: center; gap: 14px;
  }
  .brand__dot {
    width: 40px; height: 40px; border-radius: 50%;
    background: var(--brand-purple);
  }
  .brand__name {
    font-size: 36px; font-weight: 600; color: var(--text-grey);
    letter-spacing: 0.5px;
  }
  .contact-band {
    position: absolute; left: 0; right: 0; top: 178px; height: 104px;
    background: var(--band-grey);
    display: flex; align-items: center;
  }
  .holder-name {
    width: 250px; padding-left: 34px; padding-top: 30px;
    color: var(--white); font-size: 20px; font-weight: 600;
  }
  .contact-divider {
    width: 1px; height: 74px; background: var(--white); opacity: 0.85;
  }
  .contact-list { list-style: none; padding-left: 16px; }
  .contact-list li {
    display: flex; align-items: center; gap: 8px;
    color: var(--white); font-size: 15px; line-height: 25px;
  }
  .contact-list svg { width: 12px; height: 12px; fill: var(--white); }
  .web-strip {
    position: absolute; left: 0; right: 0; bottom: 0; height: 54px;
    display: flex; align-items: center; justify-content: center;
    font-size: 13.5px; font-weight: 600; letter-spacing: 3px; color: var(--text-dark);
  }
  .web-strip .web-strip__grey { color: var(--text-grey); }
  .web-strip .web-strip__purple { color: var(--brand-purple); }
  /* Back */
  .card--back { left: 630px; background: var(--card-grey); }
  .back-brand {
    position: absolute; left: 0; right: 0; top: 64px;
    display: flex; align-items: center; justify-content: center; gap: 14px;
  }
  .back-brand .brand__dot { width: 52px; height: 52px; }
  .back-brand .brand__name { color: var(--white); font-size: 34px; }
  .services-title {
    position: absolute; left: 0; right: 0; top: 172px;
    text-align: center; color: var(--white);
    font-size: 22px; font-weight: 600; letter-spacing: 2.5px;
  }
  .services {
    position: absolute; left: 0; right: 0; top: 216px;
    display: flex; justify-content: center;
  }
  .services__col { list-style: none; width: 180px; }
  .services__col--left { text-align: right; padding-right: 14px; }
  .services__col--right { padding-left: 14px; }
  .services__divider { width: 1px; background: var(--white); opacity: 0.85; }
  .services__col li {
    color: var(--white); font-size: 16px; line-height: 23px;
  }
  .services__col li::before { content: "\2714\00a0"; font-size: 11px; }
</style>
</head>
<body>
  <section class="card card--front" aria-label="Business card front">
    <div class="brand">
      <span class="brand__dot"></span>
      <span class="brand__name">Copperfield Sound</span>
    </div>
    <div class="contact-band">
      <p class="holder-name">Benedict Thornbury</p>
      <span class="contact-divider"></span>
      <ul class="contact-list">
        <li><svg viewBox="0 0 12 12"><path d="M2.5 0.8 4.3 3 3.3 4.4c0.7 1.6 2 2.9 3.6 3.6L8.3 7l2.2 1.8-1.2 2.3C4.6 10.8 1.2 7.4 0.6 2.3Z"/></svg>0330 411 7785</li>
        <li><svg viewBox="0 0 12 12"><path d="M3 0h6v12H3Zm1 1.5v7.5h4V1.5Zm2 8.6a0.7 0.7 0 1 0 0.01 0Z" fill-rule="evenodd"/></svg>07914 362 517</li>
        <li><svg viewBox="0 0 12 12"><path d="M0 2h12v8H0Zm1 1v0.4l5 3.4 5-3.4V3Zm0 1.6V9h10V4.6L6 8 1 4.6Z" fill-rule="evenodd"/></svg>ben@copperfieldsound-example.com</li>
      </ul>
    </div>
    <p class="web-strip">www.<span class="web-strip__grey">copperfield</span><span class="web-strip__purple">sound</span>-example.com</p>
  </section>

  <section class="card card--back" aria-label="Business card back">
    <div class="back-brand">
      <span class="brand__dot"></span>
      <span class="brand__name">Copperfield Sound</span>
    </div>
    <h2 class="services-title">Services We Provide</h2>
    <div class="services">
      <ul class="services__col services__col--left">
        <li>Lighting</li>
        <li>Sound</li>
        <li>Event Production</li>
        <li>Staging</li>
      </ul>
      <span class="services__divider"></span>
      <ul class="services__col services__col--right">
        <li>LED Uplighting</li>
        <li>Projection Mapping</li>
        <li>Wedding Hire</li>
      </ul>
    </div>
  </section>
</body>
</html>
```